Business Card for a finance professional

I need a business card design to introduce myself to a professional networking (mainly banks) and potential companies to hire and remember me. I would like to use black, grey, white and maybe gold/silver colors and maybe something with my initials(R L F P T). The final design should communicate seriousness, profissionalism and something innovative.

The basic informations in the card are: Name, e-mail, phone number and trabnet. (I'm thinking to put some directly short link to my trabnet account or maybe some app - non QR Code - to add my contacts to a phone directly.)

My name is Mariana Lopes Ferreira Pinto dos Reis (I prefer to use only 'Mariana Lopes' or 'Mariana Reis' but i'm open to other suggestions) and I have 26 years old (just if it helps to build based in my age).
Updates

Dear designers, I wish to thank your participation in this project! It was very difficult to choose one! Thank your for your work! Best regards and success. Mariana

Target Market(s)

Potential hires and big companies.

Industry/Entity Type

Finance

Requirements
Must have
• The informations required at the business card are:
Name: Mariana Lopes F. P. dos Reis
Email: mariana.lop.reis@quellomail.com
Phone: +55 61 8493 5710
TrabNet: http://br.trabnet-perfis.com/in/marianalr/
Nice to have
• Modern and innovative look.
I suggest to use the colors black, grey, white, gold and/or silver, but I'm open to other colors.
Should not have
• A message showing that I need to be hired. It's more to "know me and remember me" than "hire me please".

```html
<!DOCTYPE html>
<html lang="en">
<head>
<meta charset="utf-8">
<title>Mariana Reis – Business Card</title>
<link rel="stylesheet" href="https://fonts.googleapis.com/css2?family=Open+Sans:wght@300;400&display=swap">
<style>
  :root {
    --page: #ffffff;
    --card: #000000;
    --text-light: #c8c8c8;
    --text-soft: #a9a9a9;
    --divider: #2b2b2b;
    --sq-1: #2c2c2c;
    --sq-2: #3a3a3a;
    --sq-3: #4a4a4a;
    --sq-4: #5c5c5c;
  }
  * { margin: 0; padding: 0; box-sizing: border-box; }
  html, body {
    width: 1200px; height: 338px; overflow: hidden;
    background: var(--page);
    font-family: "Open Sans", sans-serif;
  }
  .canvas { position: relative; width: 1200px; height: 338px; }
  .card {
    position: absolute; top: 0; height: 338px;
    background: var(--card); overflow: hidden;
  }
  .card--front { left: 0; width: 570px; }
  .card--back { left: 594px; width: 606px; }
  .squares { position: absolute; }

  .front-name {
    position: absolute; left: 40px; top: 138px;
    font-weight: 300; font-size: 55px; line-height: 1;
    color: var(--text-light); white-space: nowrap;
    letter-spacing: -0.5px;
  }
  .front-name-reflection {
    position: absolute; left: 40px; top: 196px;
    font-weight: 300; font-size: 55px; line-height: 1;
    color: var(--text-light); white-space: nowrap;
    letter-spacing: -0.5px;
    transform: scaleY(-1);
    opacity: 0.28;
    -webkit-mask-image: linear-gradient(to top, rgba(0,0,0,1), rgba(0,0,0,0) 60%);
    mask-image: linear-gradient(to top, rgba(0,0,0,1), rgba(0,0,0,0) 60%);
  }

  .back-name {
    position: absolute; left: 42px; top: 76px;
    font-weight: 300; font-size: 26px; color: var(--text-light);
    white-space: nowrap;
  }
  .divider {
    position: absolute; left: 300px; top: 0; width: 5px; height: 338px;
    background: var(--divider);
  }
  .contact {
    position: absolute; left: 318px; top: 14px; right: 0;
    color: var(--text-soft); font-weight: 400;
  }
  .contact-name { font-size: 27px; font-weight: 300; color: var(--text-light); line-height: 1.15; }
  .contact-phone { font-size: 19px; line-height: 1.3; }
  .contact-links { margin-top: 30px; font-size: 19px; line-height: 1.45; white-space: nowrap; }
  .tagline {
    position: absolute; left: 318px; bottom: 8px;
    font-size: 22px; font-weight: 300; color: var(--text-light);
    white-space: nowrap;
  }
</style>
</head>
<body>
<main class="canvas">
  <section class="card card--front" aria-label="Card front">
    <svg class="squares" style="left:0;top:0" width="180" height="140" viewBox="0 0 180 140" aria-hidden="true">
      <rect x="0" y="58" width="40" height="62" fill="var(--sq-1)"/>
      <rect x="24" y="10" width="44" height="44" fill="var(--sq-3)"/>
      <rect x="58" y="70" width="56" height="56" fill="var(--sq-2)"/>
      <rect x="88" y="42" width="80" height="80" fill="var(--sq-4)"/>
    </svg>
    <div class="front-name">Mariana Reis</div>
    <div class="front-name-reflection" aria-hidden="true">Mariana Reis</div>
    <svg class="squares" style="left:430px;top:256px" width="120" height="82" viewBox="0 0 120 82" aria-hidden="true">
      <rect x="4" y="8" width="40" height="40" fill="var(--sq-4)"/>
      <rect x="48" y="6" width="44" height="44" fill="var(--sq-2)"/>
      <rect x="24" y="42" width="44" height="40" fill="var(--sq-3)"/>
      <rect x="74" y="46" width="34" height="34" fill="var(--sq-1)"/>
    </svg>
  </section>

  <section class="card card--back" aria-label="Card back">
    <svg class="squares" style="left:30px;top:6px" width="80" height="70" viewBox="0 0 80 70" aria-hidden="true">
      <rect x="6" y="4" width="34" height="34" fill="var(--sq-2)"/>
      <rect x="30" y="22" width="38" height="38" fill="var(--sq-4)"/>
      <rect x="0" y="34" width="28" height="28" fill="var(--sq-1)"/>
    </svg>
    <div class="back-name">Mariana Reis</div>
    <svg class="squares" style="left:226px;top:122px" width="64" height="46" viewBox="0 0 64 46" aria-hidden="true">
      <rect x="2" y="12" width="24" height="24" fill="var(--sq-3)"/>
      <rect x="24" y="2" width="28" height="28" fill="var(--sq-4)"/>
      <rect x="30" y="24" width="22" height="20" fill="var(--sq-2)"/>
    </svg>
    <div class="divider"></div>
    <div class="contact">
      <p class="contact-name">Mariana Reis</p>
      <p class="contact-phone">+44 80416</p>
      <p class="contact-links">marianareis@quellomail.com<br>@trabnet</p>
    </div>
    <p class="tagline">Professional Networking</p>
  </section>
</main>
</body>
</html>
```